amber crest health and wellness group.

need a full website design , all information provided in word document labeled website blue print

Target Market(s)

first responders, military , people in crisis

Coding

Coded - Design and coding required

Number of Pages Required

1 page

```html
<!DOCTYPE html>
<html lang="en">
<head>
<meta charset="utf-8">
<title>Amber Crest Health &amp; Wellness Group</title>
<link rel="stylesheet" href="https://fonts.googleapis.com/css2?family=Jost:wght@400;500&family=Playfair+Display:wght@400&display=swap">
<style>
:root{
  --ink:#0b0b0b;
  --white:#ffffff;
  --cyan:#00c6f2;
  --navy:#2b5b94;
  --navy-deep:#244f84;
  --text-dark:#1e1e1e;
  --logo-blue:#2f6fb5;
  --grey:#9a9a9a;
}
*{margin:0;padding:0;box-sizing:border-box}
html,body{width:1200px;height:3172px;overflow:hidden}
body{position:relative;background:var(--white);font-family:"Jost",sans-serif;color:var(--text-dark)}
.abs{position:absolute}
.serif{font-family:"Playfair Display",serif;font-weight:400}
.btn{position:absolute;display:flex;align-items:center;justify-content:center;border-radius:20px;font-size:13px;font-family:"Jost",sans-serif}
.btn-cyan{background:var(--cyan);color:var(--white)}
.btn-white{background:var(--white);color:var(--ink)}
.photo{position:absolute}

/* header */
.site-header{position:absolute;left:0;top:0;width:1200px;height:80px;background:var(--ink)}
.brand{position:absolute;left:150px;top:20px;width:110px;text-align:center;color:var(--logo-blue);font-size:15px;font-weight:500;letter-spacing:.5px;line-height:1.1}
.brand small{display:block;font-size:6px;letter-spacing:.6px;color:var(--logo-blue);font-weight:400}
.brand .mark{display:block;width:22px;height:22px;margin:0 auto 3px;border-radius:50%;background:#8d939b}
.main-nav{position:absolute;top:30px;color:var(--white);font-size:13px}
.main-nav span{position:absolute;white-space:nowrap}

/* hero */
.hero{position:absolute;left:0;top:80px;width:1200px;height:573px;background:linear-gradient(100deg,#3d3a35 0%,#6b655b 30%,#4a4740 55%,#2b2925 80%,#1c1b19 100%)}
.hero-shade{position:absolute;inset:0;background:linear-gradient(180deg,rgba(0,0,0,.05) 0%,rgba(0,0,0,.35) 55%,rgba(0,0,0,.75) 100%)}
.hero-title{position:absolute;left:0;width:1200px;top:215px;text-align:center;color:var(--white);font-size:56px;line-height:57px}
.hero-lead{position:absolute;left:0;width:1200px;top:350px;text-align:center;color:var(--white);font-size:13px;line-height:18px}

/* about */
.about{position:absolute;left:0;top:653px;width:1200px;height:569px;background:radial-gradient(ellipse at 30% 40%,#3265a0 0%,var(--navy) 50%,var(--navy-deep) 100%)}
.section-title{font-size:56px;line-height:1;color:var(--white)}
.body-copy{font-size:12.5px;line-height:17px}
.body-copy p+p{margin-top:17px}

/* services */
.services-band{position:absolute;left:0;top:1673px;width:1200px;height:387px;background:radial-gradient(ellipse at 50% 30%,#2a2a2a 0%,#141414 60%,#070707 100%)}
.service-card{position:absolute;display:flex;align-items:flex-end;justify-content:center;padding-bottom:22px;color:var(--white);font-size:18px}

/* mission */
.mission-panel{position:absolute;left:600px;top:2403px;width:600px;height:362px;background:linear-gradient(135deg,#10cdf5 0%,var(--cyan) 60%,#06bde8 100%)}

/* partners */
.partner{position:absolute;top:2828px;display:flex;align-items:center;gap:7px;font-size:16px;font-weight:500;color:#1f2a44}
.partner i{display:block;width:18px;height:18px;background:#1f2a44}
.partner i.round{border-radius:50%}

/* footer */
.site-footer{position:absolute;left:0;top:2910px;width:1200px;height:262px;background:var(--ink)}
.footer-nav{position:absolute;top:3090px;color:var(--white);font-size:13px}
.footer-nav span{position:absolute;white-space:nowrap}
.social{position:absolute;top:3043px;width:25px;height:25px;border:1.5px solid var(--white);border-radius:50%}
.copyright{position:absolute;left:0;width:1200px;top:3147px;text-align:center;color:var(--white);font-size:10px}
</style>
</head>
<body>

<header class="site-header">
  <div class="brand"><span class="mark"></span>AMBER CREST<small>HEALTH &amp; WELLNESS GROUP</small></div>
  <nav class="main-nav">
    <span style="left:368px">Home</span>
    <span style="left:436px">About Us</span>
    <span style="left:521px">Services</span>
    <span style="left:602px">Our Team</span>
    <span style="left:690px">Join Our Team</span>
    <span style="left:804px">FAQ</span>
  </nav>
  <div class="btn btn-cyan" style="left:921px;top:18px;width:129px;height:39px">Contact</div>
</header>

<section class="hero">
  <div class="photo" role="img" aria-label="Counsellor talking with a young couple in a sunlit therapy room" style="inset:0;background:linear-gradient(100deg,#3d3a35 0%,#6b655b 30%,#4a4740 55%,#2b2925 80%,#1c1b19 100%)"></div>
  <div class="hero-shade"></div>
  <svg class="abs" style="left:127px;top:250px" width="62" height="40" viewBox="0 0 62 40" fill="none" stroke="#fff" stroke-width="2.5"><circle cx="42" cy="20" r="16"/><path d="M4 20h40M14 10 4 20l10 10"/></svg>
  <svg class="abs" style="left:1010px;top:250px" width="62" height="40" viewBox="0 0 62 40" fill="none" stroke="#fff" stroke-width="2.5"><circle cx="20" cy="20" r="16"/><path d="M18 20h40M48 10l10 10-10 10"/></svg>
  <h1 class="hero-title serif">Helping Those Who<br>Help Others</h1>
  <p class="hero-lead">Lorem ipsum dolor sit amet, consectetur adipiscing elit, sed do eiusmod<br>tempor incididunt ut labore et dolore magna aliqua.</p>
  <div class="btn btn-cyan" style="left:464px;top:399px;width:128px;height:38px">Contact</div>
  <div class="btn btn-white" style="left:607px;top:399px;width:128px;height:38px">Read More</div>
</section>

<section class="about">
  <div class="abs" style="left:149px;top:41px;width:67px;height:64px;background:var(--white)"></div>
  <div class="photo" role="img" aria-label="Therapist with notebook seated in a leather armchair" style="left:166px;top:55px;width:340px;height:339px;background:linear-gradient(160deg,#e9e6e1 0%,#cfc8bd 45%,#6a5546 100%)"></div>
  <div class="photo" role="img" aria-label="Counsellor taking notes during a session with two clients" style="left:322px;top:299px;width:269px;height:178px;border:3px solid var(--white);background:linear-gradient(120deg,#8a7a6a 0%,#c9bfb2 50%,#e3ddd4 100%)"></div>
  <svg class="abs" style="left:433px;top:365px" width="46" height="46" viewBox="0 0 46 46" fill="none" stroke="#fff" stroke-width="2.5"><circle cx="23" cy="23" r="20"/><path d="M18 14l13 9-13 9z"/></svg>
  <h2 class="section-title serif abs" style="left:622px;top:92px">About Us</h2>
  <div class="body-copy abs" style="left:622px;top:164px;width:430px;color:var(--white)">
    <p>Lorem ipsum dolor sit amet, consectetur adipiscing elit. Pellentesque eget nibh vitae metus viverra ultrices. Ut placerat luctus lorem at malesuada. Phasellus in enim nec turpis efficitur consequat eu at nibh. In eget fermentum ligula, a consectetur dolor.</p>
    <p>Aenean condimentum condimentum vehicula. Lorem ipsum dolor sit amet, consectetur adipiscing elit. Pellentesque eget nibh vitae metus viverra ultrices. Ut placerat luctus lorem at malesuada. Phasellus in enim nec turpis efficitur consequat eu at nibh. In eget fermentum ligula, a consectetur dolor. Aenean condimentum condimentum vehicula.</p>
  </div>
  <div class="btn btn-white" style="left:622px;top:377px;width:128px;height:39px">Read more</div>
</section>

<section class="who-we-serve">
  <div class="abs" style="left:971px;top:1513px;width:96px;height:96px;background:var(--cyan)"></div>
  <div class="photo" role="img" aria-label="Doctor reviewing brain scans on monitors" style="left:695px;top:1172px;width:353px;height:421px;background:linear-gradient(150deg,#0f2a55 0%,#1f4f8c 45%,#3d79b8 75%,#9fbddc 100%)"></div>
  <h2 class="serif abs" style="left:150px;top:1302px;font-size:40px;color:var(--ink)">Who We Serve</h2>
  <div class="body-copy abs" style="left:150px;top:1370px;width:470px;color:var(--text-dark)">
    <p>In ligula lacus, cursus nec consectetur ac, ornare eget nulla. Proin eget purus vitae tellus tempor feugiat non ac nibh. Vivamus sit amet sapien vel velit bibendum sollicitudin congue quis felis. Nullam eu euismod purus. Nulla diam massa, condimentum quis neque ut, consequat efficitur nisi. Quisque in erat eget ipsum tristique consectetur. Nam et luctus orci. Sed varius faucibus auctor.</p>
    <p>Vestibulum ante ipsum primis in faucibus orci luctus et ultrices posuere cubilia curae; Quisque rhoncus non tellus vitae ornare. Donec sit amet dolor fringilla, lobortis lacus ac, facilisis magna.</p>
  </div>
  <div class="btn btn-cyan" style="left:150px;top:1557px;width:130px;height:40px">Read more</div>
</section>

<section class="services">
  <div class="services-band"></div>
  <h2 class="serif abs" style="left:0;width:1200px;top:1752px;text-align:center;font-size:40px;color:var(--white)">Our Services</h2>
  <div class="service-card" role="img" aria-label="Therapist counselling a distressed client" style="left:182px;top:1900px;width:236px;height:320px;background:linear-gradient(180deg,#a7a39a 0%,#6f6a61 55%,#1c1b19 100%)">Mental Health Therapy</div>
  <div class="service-card" role="img" aria-label="Paramedic attending to a patient on a stretcher" style="left:439px;top:1841px;width:321px;height:437px;background:linear-gradient(180deg,#d9d4cc 0%,#b8463e 40%,#6b3a3a 70%,#1e1e22 100%)">Trauma &amp; First Responder support</div>
  <div class="service-card" role="img" aria-label="Hand sprinkling salt in a candlelit spa" style="left:781px;top:1900px;width:236px;height:320px;background:linear-gradient(180deg,#e7d8c8 0%,#b58b68 45%,#5a3c28 100%)">Salt Therapy</div>
  <svg class="abs" style="left:554px;top:2314px" width="42" height="26" viewBox="0 0 42 26" fill="none" stroke="#111" stroke-width="2"><circle cx="29" cy="13" r="10"/><path d="M3 13h28M10 6 3 13l7 7"/></svg>
  <svg class="abs" style="left:606px;top:2314px" width="42" height="26" viewBox="0 0 42 26" fill="none" stroke="#9a9a9a" stroke-width="2"><circle cx="13" cy="13" r="10"/><path d="M11 13h28M32 6l7 7-7 7"/></svg>
</section>

<section class="mission">
  <div class="photo" role="img" aria-label="Counsellor shaking hands with a smiling couple in a living room" style="left:0;top:2403px;width:600px;height:362px;background:linear-gradient(110deg,#4a4a4a 0%,#c9b9a6 40%,#e6ddd0 70%,#8f8070 100%)"></div>
  <div class="mission-panel"></div>
  <h2 class="serif abs" style="left:618px;top:2465px;font-size:40px;color:var(--white)">Mission &amp; Vision</h2>
  <div class="body-copy abs" style="left:621px;top:2530px;width:430px;color:var(--white)">
    <p>In ligula lacus, cursus nec consectetur ac, ornare eget nulla. Proin eget purus vitae tellus tempor feugiat non ac nibh. Vivamus sit amet sapien vel velit bibendum sollicitudin congue quis felis. Nullam eu euismod purus. Nulla diam massa, condimentum quis neque ut, consequat.</p>
    <p>Quisque in erat eget ipsum tristique consectetur. Nam et luctus orci. Sed varius faucibus auctor.</p>
  </div>
  <div class="btn btn-white" style="left:621px;top:2678px;width:128px;height:39px">Read more</div>
</section>

<section class="partners">
  <div class="partner" style="left:160px"><i></i>Northvale</div>
  <div class="partner" style="left:318px"><i class="round"></i>Harborline</div>
  <div class="partner" style="left:480px"><i class="round"></i>Tidewell</div>
  <div class="partner" style="left:588px"><i class="round"></i>Brightfort</div>
  <div class="partner" style="left:751px"><i></i>Northvale</div>
  <div class="partner" style="left:923px"><i class="round"></i>Harborline</div>
</section>

<footer class="site-footer"></footer>
<div class="abs" style="left:560px;top:2935px;width:80px;height:80px;display:flex;align-items:center;justify-content:center"><span style="display:block;width:46px;height:46px;border-radius:50%;background:#8d939b"></span></div>
<div class="abs" style="left:0;width:1200px;top:3012px;text-align:center;color:var(--logo-blue);font-size:20px;font-weight:500;letter-spacing:.5px;line-height:1">AMBER CREST<br><span style="font-size:7px;letter-spacing:.8px;font-weight:400">HEALTH &amp; WELLNESS GROUP</span></div>
<span class="social" style="left:550px"></span>
<span class="social" style="left:587px"></span>
<span class="social" style="left:624px"></span>
<nav class="footer-nav">
  <span style="left:331px">Home</span>
  <span style="left:398px">About Us</span>
  <span style="left:483px">Services</span>
  <span style="left:564px">Our Team</span>
  <span style="left:652px">Join Our Team</span>
  <span style="left:766px">Contact</span>
  <span style="left:843px">FAQ</span>
</nav>
<div class="abs" style="left:0;top:3135px;width:1200px;height:1px;background:#3a3a3a"></div>
<p class="copyright">Copyright © 2025 amber crest health and wellness group. All rights reserved.</p>

</body>
</html>
```